BRIGHT PEAK POWER.

I'd like my business logo.
contact name: Daniel Fitzhume
phone:0407395182
email: info@brightpeakpower.net.au
website: www.brightpeakpower.net.au

services:
solar
battery storage
LED lighting
energy saving solutions
general electrical
I'd like the design to look professional

Target Market(s)

Everyone

Industry/Entity Type

Business

Contact Information for Business Card

as described above

Requirements
Must have
• Id like the colours and the design to work well with my logo.

```html
<!DOCTYPE html>
<html lang="en">
<head>
<meta charset="utf-8">
<title>Bright Peak Power – Business Card</title>
<link rel="stylesheet" href="https://fonts.googleapis.com/css2?family=Lato:wght@400;700;900&display=swap">
<style>
  :root {
    --backdrop: #2b2b2b;
    --card: #fbfbfb;
    --green: #6aab2a;
    --green-dark: #5a9a22;
    --orange: #e5861a;
    --ink: #2e2e2e;
    --muted: #4a4a4a;
    --emblem-warm: rgba(236, 205, 150, 0.35);
    --emblem-green: rgba(170, 205, 150, 0.3);
  }
  * { box-sizing: border-box; margin: 0; padding: 0; }
  html, body {
    width: 1200px; height: 873px; overflow: hidden;
    background: var(--backdrop);
    font-family: "Lato", Arial, sans-serif;
  }
  .canvas { position: relative; width: 1200px; height: 873px; }
  .card {
    position: absolute; left: 150px; top: 176px;
    width: 900px; height: 520px;
    background: var(--card);
    border-radius: 22px;
    overflow: hidden;
  }
  .brand {
    position: absolute; left: 70px; top: 92px;
    display: flex; align-items: center; gap: 16px;
  }
  .brand-dot {
    width: 56px; height: 56px; border-radius: 50%;
    background: var(--orange);
  }
  .brand-name {
    font-weight: 900; font-size: 38px; line-height: 1;
    color: var(--green); letter-spacing: 0.5px;
  }
  .emblem {
    position: absolute; left: 520px; top: 40px;
    width: 330px; height: 330px; border-radius: 50%;
    background: radial-gradient(circle at 60% 60%, var(--emblem-green) 0 45%, var(--emblem-warm) 46% 70%, transparent 71%);
  }
  .person {
    position: absolute; left: 640px; top: 182px; text-align: right;
  }
  .person-name { font-weight: 700; font-size: 26px; color: var(--green-dark); }
  .person-role { font-size: 17px; color: var(--ink); margin-top: 2px; }
  .contact {
    position: absolute; left: 78px; top: 312px;
    display: flex; flex-direction: column; gap: 10px;
  }
  .contact-line { display: flex; align-items: center; gap: 10px; font-size: 21px; color: var(--ink); }
  .contact-line svg { width: 20px; height: 20px; fill: var(--orange); flex: none; }
  .website { font-weight: 900; font-size: 24px; color: var(--green); margin-top: 8px; }
  .services {
    position: absolute; left: 78px; bottom: 58px;
    font-weight: 700; font-size: 20px; color: var(--orange);
    word-spacing: 2px;
  }
  .services .sep { color: var(--green); margin: 0 10px; }
</style>
</head>
<body>
<main class="canvas">
  <section class="card">
    <div class="brand">
      <span class="brand-dot"></span>
      <span class="brand-name">Bright Peak Power</span>
    </div>

    <div class="emblem" role="img" aria-label="Faint brand emblem watermark"></div>

    <div class="person">
      <p class="person-name">Daniel Fitzhume</p>
      <p class="person-role">Owner / Founder</p>
    </div>

    <div class="contact">
      <p class="contact-line">
        <svg viewBox="0 0 24 24" aria-hidden="true"><path d="M6.6 10.8c1.4 2.8 3.8 5.1 6.6 6.6l2.2-2.2c.3-.3.7-.4 1-.2 1.1.4 2.3.6 3.6.6.6 0 1 .4 1 1V20c0 .6-.4 1-1 1C10.6 21 3 13.4 3 4c0-.6.4-1 1-1h3.5c.6 0 1 .4 1 1 0 1.3.2 2.5.6 3.6.1.3 0 .7-.2 1L6.6 10.8z"/></svg>
        0407395182
      </p>
      <p class="contact-line">
        <svg viewBox="0 0 24 24" aria-hidden="true"><path d="M2 5h20v14H2V5zm2 2v.5l8 5 8-5V7H4zm0 2.8V17h16V9.8l-8 5-8-5z"/></svg>
        info@brightpeakpower.net.au
      </p>
      <p class="website">www.brightpeakpower.net.au</p>
    </div>

    <p class="services">Solar<span class="sep">/</span>Battery Storage<span class="sep">/</span>LED Lighting<span class="sep">/</span>Energy Saving Solutions</p>
  </section>
</main>
</body>
</html>
```